Tall Pine Construction Need an information and interactive website with client portal. We have ou

Need to have a client log in screen for work orders and estimate requests.
Nice informational landing page.

Tall Pine is a full service general contractor servicing apartment complexes;
maintenance of grounds and apartments - remodeling and construction.

Design Specifics: We are pretty open here. Some good examples are
www.halvexworks.com , lorrenhousing.com and www.quin7renovate.com

For the site we need:
Homepage - to explain services
Roofing page
Apartment Page
Client Portal - where clients can set up accounts to set up work/estimate request that will be routed to our email

--Will need coding, plan to host site on Wordpress

Target Market(s)

Multi family, Residential and commercial clients

Industry/Entity Type

Construction

Coding

Coded - Design and coding required

Number of Pages Required

3 page

Font styles to use
Serif

Requirements
Must have
• Client portal
Nice to have
• Not sure. please advise

```html
<!DOCTYPE html>
<html lang="en">
<head>
<meta charset="utf-8">
<title>Client Portal – Tall Pine Construction</title>
<link rel="stylesheet" href="https://fonts.googleapis.com/css2?family=Montserrat:wght@600;700&family=Open+Sans:wght@400;600&display=swap">
<style>
:root{
  --red:#d10a0a;
  --orange:#f07b05;
  --ink:#555555;
  --nav:#4a4a4a;
  --text:#777777;
  --line:#d4d4d4;
  --footer:#1c1c1c;
  --footer-bottom:#141414;
  --footer-head:#d6d6d6;
  --footer-text:#a8a8a8;
  --icon:#6e6e6e;
}
*{margin:0;padding:0;box-sizing:border-box}
html,body{width:1200px;height:1046px;overflow:hidden;background:#fff}
body{position:relative;font-family:"Open Sans",sans-serif;color:var(--text)}
.abs{position:absolute}
.site-header{position:absolute;left:0;top:0;width:1200px;height:79px;border-bottom:1px solid #e3e3e3}
.brand{position:absolute;left:99px;top:27px;display:flex;align-items:center;gap:8px;font-family:"Montserrat",sans-serif;font-weight:700;font-size:20px;color:var(--red);letter-spacing:.5px}
.brand-mark{width:14px;height:14px;background:var(--red)}
.nav a{position:absolute;top:35px;font-family:"Montserrat",sans-serif;font-weight:600;font-size:11.5px;color:var(--nav);text-decoration:none}
.nav a.active::after{content:"";position:absolute;left:0;right:0;top:24px;height:3px;background:var(--red)}
.page-title{left:99px;top:131px;font-family:"Montserrat",sans-serif;font-weight:700;font-size:26px;color:var(--ink)}
.title-bar{left:99px;top:176px;width:43px;height:3px;background:var(--red)}
.intro{left:99px;top:198px;width:1000px;font-size:12.5px;line-height:25px}
.login-card{left:355px;top:317px;width:490px;height:304px;border:2px solid #e0e0e0;border-radius:3px}
.login-title{left:355px;top:345px;width:490px;text-align:center;font-family:"Montserrat",sans-serif;font-weight:700;font-size:25px;color:var(--ink)}
.field{left:409px;width:382px;height:43px;border:1px solid var(--line);border-radius:3px;padding:0 17px;display:flex;align-items:center;font-size:12.5px;color:#777}
.forgot{left:412px;top:538px;font-size:12.5px;color:var(--orange)}
.register{left:412px;top:563px;font-size:12.5px;color:var(--red);text-decoration:underline}
.submit{left:658px;top:536px;width:133px;height:42px;background:var(--red);border-radius:3px;color:#fff;font-family:"Montserrat",sans-serif;font-weight:700;font-size:13px;display:flex;align-items:center;justify-content:center}
.site-footer{left:0;top:743px;width:1200px;height:255px;background:var(--footer)}
.footer-bottom{left:0;top:998px;width:1200px;height:48px;background:var(--footer-bottom);text-align:center;font-size:9.5px;line-height:48px;color:var(--footer-text)}
.f-head{top:796px;font-family:"Montserrat",sans-serif;font-weight:700;font-size:14px;color:var(--footer-head)}
.f-list{top:829px;list-style:none;font-size:10.5px;color:var(--footer-text);line-height:24px}
.f-text{font-size:10.5px;color:var(--footer-text)}
.social{left:109px;top:863px;display:flex;gap:8.5px}
.social span{width:28px;height:28px;border-radius:50%;background:var(--icon)}
</style>
</head>
<body>
<header class="site-header">
  <div class="brand"><span class="brand-mark"></span>TALL PINE</div>
  <nav class="nav">
    <a style="left:423px">HOME</a>
    <a style="left:516px">ABOUT US</a>
    <a style="left:635px">ROOFING</a>
    <a style="left:746px">APARTMENT</a>
    <a class="active" style="left:877px">CLIENT PORTAL</a>
    <a style="left:1024px">CONTACT US</a>
  </nav>
</header>

<h1 class="abs page-title">CLIENT PORTAL</h1>
<div class="abs title-bar"></div>
<p class="abs intro">Lorem Ipsum is simply dummy text of the printing and typesetting industry. Lorem Ipsum has been the industry's standard dummy text ever since the 1500s, when an unknown printer took a galley of type and scrambled it to make a type specimen book. It has survived not only five centuries...</p>

<div class="abs login-card"></div>
<h2 class="abs login-title">LOGIN</h2>
<div class="abs field" style="top:412px">User name</div>
<div class="abs field" style="top:472px">Password</div>
<a class="abs forgot">Forgotten password?</a>
<a class="abs register">Register Now!</a>
<div class="abs submit">SUBMIT</div>

<footer>
  <div class="abs site-footer"></div>
  <h3 class="abs f-head" style="left:107px">FOLLOW US</h3>
  <p class="abs f-text" style="left:109px;top:828px">CONNECT WITH OUR SOCIAL NETWORK</p>
  <div class="abs social"><span></span><span></span><span></span><span></span><span></span><span></span></div>

  <h3 class="abs f-head" style="left:421px">WELCOME</h3>
  <ul class="abs f-list" style="left:422px"><li>HOME</li><li>ABOUT US</li><li>ROOFING</li><li>APARTMENT</li><li>CLIENT PORTAL</li></ul>

  <h3 class="abs f-head" style="left:647px">INFORMATION</h3>
  <ul class="abs f-list" style="left:648px"><li>TERMS &amp; CONDITIONS</li><li>PRIVACY POLICY</li><li>DISCLAIMER</li><li>CONTACT US</li><li>SITEMAP</li></ul>

  <h3 class="abs f-head" style="left:880px">CONTACT INFO</h3>
  <p class="abs f-text" style="left:881px;top:830px;line-height:22px">120 STREET NAME, CITY NAME,<br>COUNTRY NAME : 985667</p>
  <svg class="abs" style="left:884px;top:884px" width="11" height="11" viewBox="0 0 24 24"><path fill="#a8a8a8" d="M6.6 10.8a15.1 15.1 0 0 0 6.6 6.6l2.2-2.2c.3-.3.7-.4 1-.2 1.1.4 2.3.6 3.6.6.6 0 1 .4 1 1V20c0 .6-.4 1-1 1A17 17 0 0 1 3 4c0-.6.4-1 1-1h3.5c.6 0 1 .4 1 1 0 1.3.2 2.5.6 3.6.1.3 0 .7-.2 1z"/></svg>
  <p class="abs f-text" style="left:905px;top:882px">( 555 ) 014- 2230</p>
  <svg class="abs" style="left:884px;top:913px" width="12" height="10" viewBox="0 0 24 20"><rect x="1.5" y="1.5" width="21" height="17" rx="1.5" fill="none" stroke="#a8a8a8" stroke-width="2.5"/><path d="M2 3l10 8 10-8" fill="none" stroke="#a8a8a8" stroke-width="2.5"/></svg>
  <p class="abs f-text" style="left:905px;top:910px">INFO@TALLPINEWORKS.COM</p>

  <div class="abs footer-bottom">COPYRIGHT © 2016. TALL PINE CONSTRUCTIONS. ALL RIGHTS RESERVED.</div>
</footer>
</body>
</html>
```